Corvanta512 Business Card Redesign

I want to create a design for brand new business cards, I need something exceptional for clear plastic business card design. Please do not submit without it being on a clear design. Photos of the various logo versions attached.

```html
<!DOCTYPE html>
<html lang="en">
<head>
<meta charset="utf-8">
<title>Corvanta512 – Business Card</title>
<link rel="stylesheet" href="https://fonts.googleapis.com/css2?family=Open+Sans:wght@400;600;700;800&display=swap">
<style>
  :root {
    --backdrop: #93a5b3;
    --card-light: #cfdde8;
    --card-mid: #b9c8d4;
    --card-edge: #e6f2f8;
    --gold: #a38c48;
    --gold-light: #c9b878;
    --ink: #3e4448;
    --rule-dark: #4a4f52;
  }
  * { margin: 0; padding: 0; box-sizing: border-box; }
  html, body {
    width: 1200px;
    height: 927px;
    overflow: hidden;
    background: var(--backdrop);
    font-family: "Open Sans", sans-serif;
  }
  .card {
    position: absolute;
    left: 195px;
    top: 231px;
    width: 811px;
    height: 465px;
    border: 2px solid var(--card-edge);
    border-radius: 3px;
    background:
      radial-gradient(ellipse 340px 420px at 160px 200px, rgba(220,235,245,0.7), transparent 70%),
      radial-gradient(ellipse 300px 240px at 300px 440px, rgba(215,232,245,0.6), transparent 70%),
      linear-gradient(135deg, var(--card-light), var(--card-mid) 55%, #bccbd7);
  }
  .holder-name {
    position: absolute;
    left: 44px;
    top: 238px;
    font-size: 35px;
    font-weight: 800;
    letter-spacing: -0.5px;
    color: var(--gold);
    line-height: 1;
  }
  .holder-title {
    position: absolute;
    left: 45px;
    top: 271px;
    font-size: 23px;
    font-weight: 400;
    color: var(--ink);
    line-height: 1.2;
  }
  .divider {
    position: absolute;
    left: 44px;
    top: 310px;
    width: 719px;
    height: 2px;
    background: linear-gradient(90deg, var(--gold) 0, var(--gold-light) 295px, var(--rule-dark) 295px);
  }
  .brand-name {
    position: absolute;
    right: 55px;
    top: 245px;
    font-size: 50px;
    font-weight: 700;
    color: var(--gold);
    line-height: 1;
    letter-spacing: 0.5px;
  }
  .contact-list {
    position: absolute;
    left: 44px;
    top: 327px;
    list-style: none;
  }
  .contact-list li {
    display: flex;
    align-items: center;
    gap: 6px;
    height: 29.5px;
    font-size: 23px;
    color: var(--ink);
  }
  .contact-list svg { width: 17px; height: 17px; flex: none; }
  .address {
    position: absolute;
    right: 45px;
    top: 356px;
    text-align: right;
    font-size: 23px;
    color: var(--ink);
    line-height: 29.5px;
    font-style: normal;
  }
</style>
</head>
<body>
  <section class="card">
    <div class="brand-name">Corvanta512</div>

    <h1 class="holder-name">DANIEL MARSH</h1>
    <p class="holder-title">Managing Director</p>

    <div class="divider"></div>

    <ul class="contact-list">
      <li>
        <svg viewBox="0 0 20 20" aria-hidden="true"><path fill="#a38c48" d="M2 7c0-2 3-4 8-4s8 2 8 4v2h-4V7.5c-1-.6-2.4-.9-4-.9s-3 .3-4 .9V9H2V7zm3 3h10l2 7H3l2-7zm5 1.5a2.3 2.3 0 100 4.6 2.3 2.3 0 000-4.6z"/></svg>
        044-123 456 789
      </li>
      <li>
        <svg viewBox="0 0 20 20" aria-hidden="true"><path fill="#a38c48" d="M2 8l8-6 8 6v10H2V8zm2 1.5V16h12V9.5l-6 4.2-6-4.2z"/></svg>
        info@webname.com
      </li>
      <li>
        <svg viewBox="0 0 20 20" aria-hidden="true"><circle cx="10" cy="10" r="8" fill="#a38c48"/><path fill="#cfdde8" d="M6 5c2 0 3 1 2.5 2.5S6 8.5 5.5 10 4 11 3.5 9.5 4 5 6 5zm6.5 4c1.5 0 3 1 2.5 3s-2 3.5-3 3.5-1-2-1.5-3S11 9 12.5 9z"/></svg>
        www.websitename.com
      </li>
    </ul>

    <address class="address">
      Your Address, City<br>
      State, Zip 0000
    </address>
  </section>
</body>
</html>
```